Day Spa Web Design Project

We just created a blog to add to our main site. We need the colors to match our main site and the look and feel of the blog to be smoother and less ameture looking, like the examples below.

Main Site, match this color scheme:
http://www.verelladayspa.com/

The project site:
http://blog.verelladayspa.com/

Our industry leaders blog site is our comparative and examples of what we need:
http://blog.relaxquester.com/
http://blog.purewellnessjournal.com/
http://thelunaretreatblog.com/ (i like the layout a lot)
http://www.kneadhaven.com/blog/

Requirements
Must have
• social sharing.
Responsive design (already has it just keep it)
appealing mobile front page

```html
<!DOCTYPE html>
<html lang="en">
<head>
<meta charset="utf-8">
<title>Verella Day Spa — Blog</title>
<link href="https://fonts.googleapis.com/css2?family=Questrial&family=PT+Sans:wght@400;700&family=Crimson+Text&family=Oswald:wght@500;600&display=swap" rel="stylesheet">
<style>
:root{
  --page-top:#e3bd88;
  --page-bottom:#f2d9ae;
  --panel:#f6e4c6;
  --card:#fbf1e3;
  --card-edge:#efe0c8;
  --ink:#2a1d10;
  --body-text:#5b4a38;
  --header-black:#050403;
  --nav-top:#4a3216;
  --nav-bottom:#1c1208;
  --button:#2f1f0f;
  --band:#4b3419;
  --footer:#3a2612;
  --accent:#f07a1c;
  --share:#b89a72;
}
*{box-sizing:border-box;margin:0;padding:0}
html,body{width:707px;height:1200px;overflow:hidden}
body{
  position:relative;
  background:linear-gradient(to bottom,var(--page-top) 0,#d9a866 90px,#f0d3a6 130px,var(--page-bottom) 100%);
  font-family:"PT Sans",sans-serif;color:var(--ink);
}
.site{position:absolute;left:42px;top:8px;width:623px;height:1192px;background:var(--panel)}
.masthead{height:74px;background:var(--header-black);border-radius:6px 6px 0 0;position:relative;color:#fff}
.brand{position:absolute;left:30px;top:20px}
.brand-name{font-family:"Questrial",sans-serif;font-size:25px;line-height:1;letter-spacing:.3px}
.brand-tag{font-family:"Questrial",sans-serif;font-size:9.5px;margin-top:3px;letter-spacing:.2px}
.call{position:absolute;right:19px;top:28px;text-align:right}
.call-label{font-size:10.5px;color:#ddd}
.call-number{font-size:17px;letter-spacing:.5px;margin-top:1px}
.main-nav{height:32px;background:linear-gradient(var(--nav-top),var(--nav-bottom));display:flex;padding-left:12px}
.main-nav a{color:#fff;text-decoration:none;font-size:10.5px;line-height:32px;padding:0 10px;border-right:1px solid #5a4126}
.main-nav a:last-child{border-right:none}
.hero{position:absolute;left:12px;top:114px;width:602px;height:190px;border:2px solid #fff6e8;
  background:linear-gradient(100deg,#8a6a4a 0%,#c49370 25%,#2b2620 45%,#3a332c 60%,#d8c9a4 78%,#f2c820 92%,#e9b315 100%)}
.section-title{position:absolute;left:18px;top:326px;font-size:15.5px;font-weight:700}
.column{position:absolute;top:354px;width:188px;display:flex;flex-direction:column;gap:7px}
.col-1{left:16px}.col-2{left:216px}.col-3{left:416px;top:356px;gap:16px}
.post{background:var(--card);border:1px solid var(--card-edge);border-bottom:4px solid #000;padding:10px 11px 12px}
.post-photo{display:block;width:100%;border:2px solid #fff}
.post-title{font-family:"Crimson Text",serif;font-size:11px;margin-top:10px;letter-spacing:.2px}
.post-excerpt{font-size:7.3px;line-height:13.5px;color:var(--body-text);margin-top:4px}
.share{display:flex;gap:3px;align-items:center;margin-top:10px}
.share span{width:13px;height:13px;background:var(--share);display:block}
.share .count{width:18px;background:#fff;border:1px solid #e3d4bd;font-size:6.5px;text-align:center;line-height:11px;color:#333;margin-left:2px}
.learn-more{display:inline-block;margin-top:10px;background:var(--button);color:#fff;font-size:7px;padding:4px 10px;text-decoration:none;border-radius:1px}
.promo{background:var(--card);border:1px solid var(--card-edge);height:89px;text-align:center;padding-top:18px;font-family:"Oswald",sans-serif}
.promo-line{font-size:11px;font-weight:500;line-height:17px;color:var(--ink)}
.promo-big{font-size:18.5px;font-weight:600;color:var(--accent);line-height:22px;margin-top:1px}
.subscribe{position:absolute;left:0;top:1064px;width:625px;height:46px;background:var(--band);display:flex;align-items:center;padding-left:129px}
.subscribe-label{color:#fff;font-size:12px;margin-right:10px}
.subscribe-input{width:164px;height:20px;background:#fbf3e6;font-size:7px;color:#555;padding-left:9px;line-height:20px}
.subscribe-button{width:54px;height:20px;background:#8b6c46;color:#fff;font-size:8px;text-align:center;line-height:20px}
.site-footer{position:absolute;left:0;top:1110px;width:625px;height:82px;background:var(--footer);color:#fff}
.footer-links{position:absolute;left:109px;top:19px;font-size:8px}
.footer-links a{color:#fff;text-decoration:none}
.footer-links i{font-style:normal;margin:0 5px}
.copyright{position:absolute;left:0;width:580px;text-align:center;top:38px;font-size:7px;color:#ddd}
.social{position:absolute;right:14px;top:17px;display:flex;gap:3px}
.social span{width:16px;height:16px;border-radius:50%;background:#fff;display:block}
</style>
</head>
<body>
<div class="site">
  <header class="masthead">
    <div class="brand">
      <div class="brand-name">Verella Day Spa</div>
      <div class="brand-tag">Natural Treatments for Body, Skin &amp; Nails</div>
    </div>
    <div class="call">
      <div class="call-label">Call Us Today</div>
      <div class="call-number">555.210.3344</div>
    </div>
  </header>
  <nav class="main-nav">
    <a href="#">Home</a><a href="#">Meet the Staff</a><a href="#">Press</a><a href="#">Tour Our Spa</a><a href="#">About</a><a href="#">Blog</a><a href="#">Spa Services</a><a href="#">Specials</a><a href="#">Contact</a>
  </nav>

  <div class="hero" role="img" aria-label="Lit candle in a dark stone bowl beside dried roses and a yellow flower"></div>

  <h2 class="section-title">Recent Blog</h2>

  <div class="column col-1">
    <article class="post">
      <div class="post-photo" role="img" aria-label="Woman relaxing during a back massage" style="height:96px;background:linear-gradient(120deg,#b9708a,#e8c8b0 50%,#f4efe9)"></div>
      <h3 class="post-title">BLOG HEADLINE HERE</h3>
      <p class="post-excerpt">Some stress is natural, but often times stress becomes a problem when it leaves you feeling overwhelmed and out of control. Seventy seven percent of Americans report experiencing phys-ical symptoms of stress, according</p>
      <div class="share" style="margin-top:22px"><span></span><span></span><span></span><span></span><span></span><span></span><b class="count">1</b></div>
      <a class="learn-more" href="#">Learn More</a>
    </article>
    <article class="post">
      <div class="post-photo" role="img" aria-label="Woman lying down with spa stones on her back" style="height:154px;background:linear-gradient(160deg,#e9cdb6,#c98f6c 55%,#8f6a4a)"></div>
      <p class="post-excerpt" style="margin-top:14px">Mauris vel lacus vitae felis vestibulum volutpat. Etiam est nunc, venenatis in, tristique eu, imperdiet ac, nisl. Cum sociis natoque penatibus et magnis dis parturient montes, nascetur ridicu-lus mus. In iaculis facilisis massa. Etiam eu urna. Sed porta. Suspendisse quam leo, molestie sed, luctus quis, feugiat in, pede. Fusce tellus.</p>
      <div class="share" style="margin-top:14px"><span></span><span></span><span></span><span></span><span></span><span></span><b class="count">1</b></div>
      <a class="learn-more" href="#">Learn More</a>
      <div style="height:20px"></div>
    </article>
  </div>

  <div class="column col-2">
    <article class="post">
      <div class="post-photo" role="img" aria-label="Woman resting on towels with a lily" style="height:95px;background:linear-gradient(100deg,#dfe9c8,#eef2e6 50%,#5f7a3a)"></div>
      <h3 class="post-title">BLOG HEADLINE HERE</h3>
      <p class="post-excerpt">Have you been paying attention to the latest spring fashion trends? If not, don't worry! We've got you covered from head to toe.</p>
      <div class="share"><span></span><span></span><span></span><span></span><span></span><span></span><b class="count">1</b></div>
      <a class="learn-more" href="#">Learn More</a>
    </article>
    <article class="post">
      <div class="post-photo" role="img" aria-label="Three models in colourful spring dresses" style="height:95px;background:linear-gradient(90deg,#e8743a,#f0c9a0 30%,#e0d080 50%,#c9d8e0 70%,#e090c0)"></div>
      <h3 class="post-title">BLOG HEADLINE HERE</h3>
      <p class="post-excerpt">unc tempus felis vitae urna. Vivamus porttitor, g, purus nisi eleifend libero, a tempus libero lectus feugiat felis.</p>
      <div class="share"><span></span><span></span><span></span><span></span><span></span><span></span><b class="count">1</b></div>
      <a class="learn-more" href="#">Learn More</a>
    </article>
    <article class="post">
      <div class="post-photo" role="img" aria-label="Stacked black stones with an orchid and bamboo leaves" style="height:86px;background:linear-gradient(170deg,#c8e09a,#f2f6ea 55%,#3a3a36)"></div>
      <h3 class="post-title">BLOG HEADLINE HERE</h3>
      <p class="post-excerpt">Spring fashion trends? If not, don't worry! We've got you covered from head to toe.</p>
      <div class="share"><span></span><span></span><span></span><span></span><span></span><span></span><b class="count">1</b></div>
      <a class="learn-more" href="#">Learn More</a>
    </article>
  </div>

  <div class="column col-3">
    <article class="post">
      <div class="post-photo" role="img" aria-label="Facial mask treatment being applied" style="height:96px;background:linear-gradient(110deg,#b88868,#f2ece6 50%,#d9c9ba)"></div>
      <h3 class="post-title">BLOG HEADLINE HERE</h3>
      <p class="post-excerpt">Some stress is natural, but often times stress becomes a problem when it leaves you feeling overwhelmed and out of control.</p>
      <div class="share"><span></span><span></span><span></span><span></span><span></span><span></span><b class="count">1</b></div>
      <a class="learn-more" href="#">Learn More</a>
    </article>
    <article class="post">
      <div class="post-photo" role="img" aria-label="Relaxing face massage with spa candles" style="height:95px;background:linear-gradient(100deg,#d8b496,#efe4da 50%,#a87a50)"></div>
      <h3 class="post-title">BLOG HEADLINE HERE</h3>
      <p class="post-excerpt">Some stress is natural, but often times stress becomes a problem when it leaves you feeling overwhelmed and out of control. Seventy seven percent of Americans report experiencing physical symptoms of stress, according to a 2012 study done by the National Wellness Council.</p>
      <div class="share"><span></span><span></span><span></span><span></span><span></span><span></span><b class="count">1</b></div>
      <a class="learn-more" href="#">Learn More</a>
    </article>
    <aside class="promo" style="margin-top:-8px">
      <div class="promo-line">FLLOW US FOR GREAT SAVINGS</div>
      <div class="promo-line">AND A CHANCE TO WIN</div>
      <div class="promo-big">SPA TREATMENTS</div>
    </aside>
  </div>

  <section class="subscribe">
    <span class="subscribe-label">FOLLOW US VIA EMAIL</span>
    <span class="subscribe-input">email address</span>
    <span class="subscribe-button">SUBMIT</span>
  </section>

  <footer class="site-footer">
    <div class="footer-links">
      <a href="#">Home</a><i>|</i><a href="#">About Us</a><i>|</i><a href="#">Spa Services</a><i>|</i><a href="#">Spa Packages</a><i>|</i><a href="#">Specials</a><i>|</i><a href="#">Gift Certificates</a><i>|</i><a href="#">Spa Policy</a><i>|</i><a href="#">Contact Us</a>
    </div>
    <div class="copyright">© Copyright 2013 Verella Day Spa | 48 Linden Grove Ave. Fairhaven, FL 33900</div>
    <div class="social"><span></span><span></span><span></span></div>
  </footer>
</div>
</body>
</html>
```